Loom Vale Wordpress Blog Page

Loom Vale is a supplier of custom printed clothing. Our E-Commerce platform uses a reverse proxy to incorporate a Wordpress Blog into the site.

E-Commerce site: http://www.loomvale-example.clothing

E-Commerce site incorporates blog page here: http://www.loomvale-example.clothing/blog

Currently running Wordpress Blog site: http://www.loomvale-example.net.au

We need our blog styled to fit in with the look and feel of the website. The Header and Footer in particular are key to the blog appearing to the user as part of the site. Some key elements may not be possible such as the shopping cart, or other dynamic elements. The rest of the blog needs to be styled to fit in with the site as much as possible.

Font styles to use
Other font styles liked:
• Headline font is HWT ARTZ

Requirements
Must have
• Styled look and feel to fit in with current site design
• Must be responsive design and mobile friendly
• Must be SEO standards compliant

```html
<!DOCTYPE html>
<html lang="en">
<head>
<meta charset="utf-8">
<title>Loom Vale Blog</title>
<link href="https://fonts.googleapis.com/css2?family=Raleway:wght@400;600;700;800&family=Open+Sans:wght@400;600;700&display=swap" rel="stylesheet">
<style>
:root{
  --navy:#0f2232;
  --navy-deep:#0a1824;
  --blue:#1f95d4;
  --blue-dark:#137ab3;
  --page:#e9edf0;
  --card:#ffffff;
  --ink:#1d2b38;
  --muted:#7b8791;
  --rule:#dde3e8;
}
*{box-sizing:border-box;margin:0;padding:0}
html,body{width:675px;height:1200px;overflow:hidden}
body{background:var(--page);font-family:"Open Sans",sans-serif;color:var(--ink);position:relative}
.wrap{width:484px;margin:0 auto;position:relative}

/* header */
.site-header{background:var(--navy);height:63px}
.site-header .wrap{display:flex;align-items:center;height:63px;justify-content:space-between}
.brand{display:flex;align-items:center;gap:6px}
.brand-dot{width:22px;height:22px;border-radius:50%;background:#fff}
.brand-name{font-family:"Raleway",sans-serif;font-weight:700;font-size:15px;color:#fff}
.search{margin-left:auto;margin-right:30px;width:120px;height:16px;background:#1b3448;border:1px solid #2b4a62;display:flex;align-items:center;justify-content:space-between;padding:0 5px;font-size:6.5px;color:#8ea3b3}
.call{text-align:right;line-height:1.1}
.call small{display:block;font-size:6.5px;color:var(--blue);font-weight:700;letter-spacing:.5px}
.call strong{font-family:"Raleway",sans-serif;font-size:13px;color:#fff;font-weight:800}

/* nav */
.main-nav{background:var(--blue);height:19px}
.main-nav ul{list-style:none;display:flex;height:19px}
.main-nav li{font-family:"Raleway",sans-serif;font-weight:700;font-size:7.5px;color:#fff;padding:0 9px;line-height:19px;letter-spacing:.3px}
.main-nav li.active{background:var(--blue-dark)}

/* hero */
.hero{margin-top:9px;height:236px;position:relative;background:linear-gradient(100deg,#6b5a4c 0%,#a58e77 35%,#c9b9a6 55%,#7d8a8c 80%,#4c5659 100%);overflow:hidden}
.hero-photo{position:absolute;inset:0}
.hero-figure{position:absolute;left:190px;top:0;width:110px;height:236px;background:linear-gradient(#6b5a4c 0,#6b5a4c 30%,#3fb08a 30%,#33a07c 100%);opacity:.75;border-radius:40px 40px 0 0}
.hero-text{position:absolute;left:0;right:0;top:118px;text-align:center;color:#fff}
.hero-text h2{font-family:"Raleway",sans-serif;font-weight:800;font-size:21px;letter-spacing:.5px;text-shadow:0 1px 3px rgba(0,0,0,.35)}
.hero-text p{font-family:"Raleway",sans-serif;font-weight:700;font-size:10px;color:#e3f0f7;margin-top:3px;letter-spacing:.6px}
.dots{position:absolute;bottom:12px;left:50%;transform:translateX(-50%);display:flex;gap:4px}
.dots i{width:6px;height:6px;border-radius:50%;background:rgba(255,255,255,.55)}
.dots i:first-child{background:#fff}

/* columns */
.content{display:flex;gap:14px;margin-top:12px}
.posts{width:336px}
.section-title{font-family:"Raleway",sans-serif;font-weight:800;font-size:12px;color:var(--blue);padding-top:9px;padding-bottom:5px;border-bottom:2px solid var(--blue);display:inline-block}
.section-rule{border-top:1px solid var(--rule);margin-top:-1px;margin-bottom:10px}
.post{display:flex;gap:14px;height:129px;padding-bottom:10px}
.post-thumb{width:117px;height:104px;flex:none}
.post-body h3{font-family:"Raleway",sans-serif;font-weight:600;font-size:11.5px;line-height:1.3;color:var(--ink)}
.post-body p{font-size:6.3px;line-height:1.55;color:var(--muted);margin-top:6px}
.post-meta{font-size:5.8px;font-weight:700;color:var(--blue);margin-top:6px;letter-spacing:.3px}
.post-meta span{color:var(--muted);margin:0 3px}

.sidebar{width:134px}
.about-photo{height:72px;background:linear-gradient(135deg,#b33a3a,#7a2a30 50%,#3a4f6a)}
.about{background:var(--blue);color:#fff;padding:8px 9px;text-align:center;height:66px}
.about h4{font-family:"Raleway",sans-serif;font-size:8px;font-weight:800;letter-spacing:.4px}
.about p{font-size:5.6px;line-height:1.5;margin-top:4px;color:#e6f3fb}
.widget{background:var(--card);margin-top:14px;padding:8px 8px 9px}
.widget h4{font-family:"Raleway",sans-serif;font-size:8px;font-weight:800;color:var(--ink);letter-spacing:.4px;padding-bottom:5px;border-bottom:1px solid var(--rule);margin-bottom:6px}
.recent{display:flex;gap:6px;align-items:center;padding:5px 0;border-bottom:1px solid #eef1f3}
.recent:last-child{border-bottom:0}
.avatar{width:24px;height:24px;border-radius:50%;background:linear-gradient(#b89a84,#6f5b4d);flex:none}
.recent p{font-size:5.6px;line-height:1.45;color:var(--muted)}
.recent b{color:var(--ink);font-weight:600}
.archives li{list-style:none;font-size:6px;color:var(--muted);line-height:2}
.testimonial{display:flex;gap:6px}
.quote{font-family:"Raleway",sans-serif;font-size:20px;font-weight:800;color:var(--blue);line-height:.8}
.testimonial p{font-size:5.6px;line-height:1.5;color:var(--muted)}
.t-dots{display:flex;gap:3px;margin-top:6px}
.t-dots i{width:5px;height:5px;border-radius:50%;background:#c6d2da}
.t-dots i:first-child{background:var(--blue)}

/* footer */
.site-footer{position:absolute;left:0;right:0;top:1024px;height:176px;background:var(--navy)}
.footer-cols{display:flex;gap:26px;padding-top:30px}
.footer-cols h5{font-family:"Raleway",sans-serif;font-size:8.5px;color:#fff;font-weight:700;margin-bottom:6px}
.footer-cols li{list-style:none;font-size:6.2px;color:#8fa2b1;line-height:1.9}
.social{display:flex;gap:6px;margin-top:5px}
.social i{width:9px;height:9px;background:var(--blue);border-radius:2px}
.footer-brand{position:absolute;right:0;top:80px;display:flex;align-items:center;gap:6px}
.footer-bottom{position:absolute;left:0;right:0;bottom:0;height:22px;background:var(--navy-deep)}
.footer-bottom .wrap{font-size:5.8px;color:#6d8293;line-height:22px}
</style>
</head>
<body>

<header class="site-header">
  <div class="wrap">
    <div class="brand"><span class="brand-dot"></span><span class="brand-name">Loom Vale</span></div>
    <div class="search"><span>Search here</span>
      <svg width="7" height="7" viewBox="0 0 10 10"><circle cx="4" cy="4" r="3" fill="none" stroke="#8ea3b3" stroke-width="1.5"/><line x1="6.3" y1="6.3" x2="9" y2="9" stroke="#8ea3b3" stroke-width="1.5"/></svg>
    </div>
    <div class="call"><small>CALL US NOW</small><strong>1300 55 01 47</strong></div>
  </div>
</header>

<nav class="main-nav">
  <div class="wrap">
    <ul>
      <li class="active">HOME</li><li>CASUAL</li><li>WORK</li><li>ACTIVE</li><li>ALL-OVER</li><li>DESIGN IDEAS</li><li>CONTACT US</li><li>GET A QUOTE</li>
    </ul>
  </div>
</nav>

<main class="wrap">
  <section class="hero">
    <div class="hero-photo" role="img" aria-label="Photo of a smiling young man in a green printed t-shirt in a warm indoor setting"></div>
    <div class="hero-text">
      <h2>DUIS QUAM NAM EGET LACUS</h2>
      <p>PRAESENT AMET EST DICTUM DOLOR DICTUM</p>
    </div>
    <div class="dots"><i></i><i></i><i></i><i></i></div>
  </section>

  <div class="content">
    <section class="posts">
      <h2 class="section-title">LATEST BLOG</h2>
      <div class="section-rule"></div>

      <article class="post">
        <div class="post-thumb" role="img" aria-label="Photo of a man in a dark printed tee" style="background:linear-gradient(#d9d6d2,#6a6560)"></div>
        <div class="post-body">
          <h3>Vestibulum ligula augue<br>bibendum accumsan</h3>
          <p>Lorem ipsum dolor sit amet, consectetur adipiscing elit sed do eiusmod tempor incididunt ut labore et dolore magna aliqua. Ut enim ad minim veniam quis nostrud exercitation ullamco laboris nisi ut aliquip ex ea commodo consequat.</p>
          <div class="post-meta">POSTED 09 AUG 2014<span>|</span>LEARN MORE</div>
        </div>
      </article>

      <article class="post">
        <div class="post-thumb" role="img" aria-label="Photo of an orange printed garment" style="background:linear-gradient(135deg,#f29a3a,#c9541d)"></div>
        <div class="post-body">
          <h3>Duis quam Nam eget lacus Aliquam<br>erat volutpat</h3>
          <p>Lorem ipsum dolor sit amet, consectetur adipiscing elit sed do eiusmod tempor incididunt ut labore et dolore magna aliqua. Ut enim ad minim veniam quis nostrud exercitation ullamco laboris nisi ut aliquip ex ea commodo consequat.</p>
          <div class="post-meta">POSTED 09 AUG 2014<span>|</span>LEARN MORE</div>
        </div>
      </article>

      <article class="post">
        <div class="post-thumb" role="img" aria-label="Photo of a person in a dark hoodie" style="background:linear-gradient(#3a3f44,#1a1d20)"></div>
        <div class="post-body">
          <h3>Morbi porta libero id ullamcorper<br>nonummy nibh ligula</h3>
          <p>Lorem ipsum dolor sit amet, consectetur adipiscing elit sed do eiusmod tempor incididunt ut labore et dolore magna aliqua. Ut enim ad minim veniam quis nostrud exercitation ullamco laboris nisi ut aliquip ex ea commodo consequat.</p>
          <div class="post-meta">POSTED 09 AUG 2014<span>|</span>LEARN MORE</div>
        </div>
      </article>

      <article class="post">
        <div class="post-thumb" role="img" aria-label="Black and white photo of a printed tee" style="background:linear-gradient(#9a9a9a,#2e2e2e)"></div>
        <div class="post-body">
          <h3>Duis non nunc Nulla rhoncus<br>dictum metus</h3>
          <p>Lorem ipsum dolor sit amet, consectetur adipiscing elit sed do eiusmod tempor incididunt ut labore et dolore magna aliqua. Ut enim ad minim veniam quis nostrud exercitation ullamco laboris nisi ut aliquip ex ea commodo consequat.</p>
          <div class="post-meta">POSTED 09 AUG 2014<span>|</span>LEARN MORE</div>
        </div>
      </article>

      <article class="post">
        <div class="post-thumb" role="img" aria-label="Photo of a cyan sports tee on white" style="background:linear-gradient(#f4f7f8,#5cc9df)"></div>
        <div class="post-body">
          <h3>Vestibulum ligula augue<br>bibendum accumsan</h3>
          <p>Lorem ipsum dolor sit amet, consectetur adipiscing elit sed do eiusmod tempor incididunt ut labore et dolore magna aliqua. Ut enim ad minim veniam quis nostrud exercitation ullamco laboris nisi ut aliquip ex ea commodo consequat.</p>
          <div class="post-meta">POSTED 09 AUG 2014<span>|</span>LEARN MORE</div>
        </div>
      </article>
    </section>

    <aside class="sidebar">
      <div class="about-photo" role="img" aria-label="Photo of a team wearing matching red printed shirts"></div>
      <div class="about">
        <h4>LITTLE ABOUT US</h4>
        <p>We print custom clothing for teams, crews and brands, with fast turnaround and quality you can feel in every thread.</p>
      </div>

      <div class="widget">
        <h4>RECENT POSTS</h4>
        <div class="recent"><span class="avatar" role="img" aria-label="Author avatar"></span><p><b>Phasellus vel arcu</b><br>Posted 09 Aug 2014<br>Lorem ipsum dolor sit</p></div>
        <div class="recent"><span class="avatar" role="img" aria-label="Author avatar"></span><p><b>Phasellus vel arcu</b><br>Posted 09 Aug 2014<br>Lorem ipsum dolor sit</p></div>
        <div class="recent"><span class="avatar" role="img" aria-label="Author avatar"></span><p><b>Phasellus vel arcu</b><br>Posted 09 Aug 2014<br>Lorem ipsum dolor sit</p></div>
      </div>

      <div class="widget">
        <h4>ARCHIVES</h4>
        <ul class="archives">
          <li>June 2014 (4)</li><li>May 2014 (3)</li><li>April 2014 (6)</li><li>March 2014 (2)</li><li>February 2014 (5)</li><li>January 2014 (3)</li><li>December 2013 (4)</li><li>November 2013 (2)</li>
        </ul>
      </div>

      <div class="widget">
        <h4>TESTIMONIALS</h4>
        <div class="testimonial">
          <span class="quote">“</span>
          <p>Great shirts, sharp prints and friendly service. Our whole club loved the new kit and we will order again next season.</p>
        </div>
        <div class="t-dots"><i></i><i></i><i></i><i></i></div>
      </div>
    </aside>
  </div>
</main>

<footer class="site-footer">
  <div class="wrap">
    <div class="footer-cols">
      <div><h5>Quick Links</h5><ul><li>Casual apparel</li><li>Workwear range</li><li>Active gear</li><li>Design ideas</li></ul></div>
      <div><h5>Sublimes</h5><ul><li>Team uniforms</li><li>Sports jerseys</li><li>Event shirts</li><li>Custom prints</li></ul></div>
      <div><h5>Support</h5><ul><li>Order help</li><li>Delivery info</li><li>Terms of use</li><li>Contact us</li></ul></div>
      <div><h5>Contact Us</h5><ul><li>12 Harbour Road, Eastvale NSW 2000</li><li>Phone: 1300 55 01 47</li><li>Email: info@loomvale-example.clothing</li></ul>
        <div class="social"><i></i><i></i><i></i></div>
      </div>
    </div>
    <div class="footer-brand"><span class="brand-dot"></span><span class="brand-name">Loom Vale</span></div>
  </div>
  <div class="footer-bottom"><div class="wrap">© 2014 Loom Vale. All rights reserved. Terms of use.</div></div>
</footer>

</body>
</html>
```